The Lantern Guide

I am a life coach specializing in helping people with depression and bipolar disorder. I would like a nice, fun design for a business card.

```html
<!DOCTYPE html>
<html lang="en">
<head>
<meta charset="UTF-8">
<title>The Lantern Guide – Business Card</title>
<link href="https://fonts.googleapis.com/css2?family=PT+Serif:wght@400;700&display=swap" rel="stylesheet">
<style>
  :root {
    --indigo: #3a35a0;
    --indigo-deep: #2c2888;
    --grey: #b9b9bc;
    --grey-light: #d9d9db;
    --paper: #f4f4f4;
    --ink-white: #ffffff;
    --stage: #e9e7e3;
  }
  * { box-sizing: border-box; margin: 0; padding: 0; }
  html, body { width: 1200px; height: 780px; overflow: hidden; }
  body {
    background: var(--stage);
    font-family: "PT Serif", Georgia, serif;
    position: relative;
  }
  .card {
    position: absolute;
    top: 235px;
    width: 530px;
    height: 310px;
    border-radius: 3px;
    overflow: hidden;
    box-shadow: 0 6px 18px rgba(0,0,0,0.18);
  }
  .card-front { left: 40px; background: var(--paper); }
  .card-back { left: 630px; background: var(--indigo); }

  /* front */
  .front-bands { position: absolute; inset: 0; }
  .brand {
    position: absolute;
    left: 34px;
    top: 44px;
    display: flex;
    align-items: center;
    gap: 14px;
  }
  .brand-dot {
    width: 46px; height: 46px; border-radius: 50%;
    background: var(--indigo);
  }
  .brand-name { color: var(--indigo); }
  .brand-the { font-size: 13px; letter-spacing: 1px; display: block; }
  .brand-main {
    font-size: 34px; line-height: 1.05; display: block;
    border-top: 1px solid var(--indigo);
    padding-top: 2px;
  }
  .name-line {
    position: absolute;
    left: 34px;
    top: 150px;
    color: var(--ink-white);
    font-size: 14px;
    letter-spacing: 1.5px;
  }
  .name-line .divider { margin: 0 8px; }
  .name-line .role { letter-spacing: 0.5px; font-size: 13px; }
  .address {
    position: absolute;
    left: 34px;
    top: 214px;
    color: var(--ink-white);
    font-size: 13px;
    line-height: 1.55;
  }
  .contacts {
    position: absolute;
    left: 230px;
    top: 204px;
    list-style: none;
    color: var(--ink-white);
    font-size: 13px;
  }
  .contacts li { display: flex; align-items: center; gap: 8px; height: 23px; }
  .contacts svg { width: 16px; height: 16px; flex: none; }

  /* back */
  .back-texture { position: absolute; inset: 0; }
  .back-brand {
    position: absolute;
    left: 0; right: 0; top: 92px;
    text-align: center;
    color: var(--ink-white);
  }
  .back-brand .brand-the { font-size: 16px; letter-spacing: 2px; }
  .back-brand .brand-main {
    font-size: 44px;
    display: inline-block;
    border-top: none;
    border-bottom: 1.5px solid var(--ink-white);
    padding: 0 4px 4px;
  }
  .back-web {
    display: block;
    margin-top: 12px;
    font-size: 13px;
    letter-spacing: 3px;
  }
</style>
</head>
<body>

<section class="card card-front" aria-label="Card front">
  <svg class="front-bands" viewBox="0 0 530 310" preserveAspectRatio="none" aria-hidden="true">
    <polygon points="0,135 530,95 530,310 0,310" fill="var(--grey)"/>
    <polygon points="0,178 530,135 530,310 0,310" fill="var(--indigo)"/>
    <path d="M400,0 C470,30 520,70 530,95 L530,0 Z" fill="var(--indigo)"/>
  </svg>

  <div class="brand">
    <span class="brand-dot" aria-hidden="true"></span>
    <span class="brand-name">
      <span class="brand-the">THE</span>
      <span class="brand-main">Lantern Guide</span>
    </span>
  </div>

  <p class="name-line">OWEN HARTLEY<span class="divider">|</span><span class="role">Managing Director</span></p>

  <p class="address">PO Box 48, Elm Row<br>Harbour Walk, Bristol</p>

  <ul class="contacts">
    <li>
      <svg viewBox="0 0 16 16" aria-hidden="true"><circle cx="8" cy="8" r="7.3" fill="none" stroke="#fff"/><rect x="5.5" y="4" width="5" height="8" rx="1" fill="none" stroke="#fff"/></svg>
      +044 210 7735
    </li>
    <li>
      <svg viewBox="0 0 16 16" aria-hidden="true"><circle cx="8" cy="8" r="7.3" fill="none" stroke="#fff"/><rect x="4" y="5" width="8" height="6" fill="none" stroke="#fff"/><path d="M4 5 L8 8.5 L12 5" fill="none" stroke="#fff"/></svg>
      hello@lanternguide.org
    </li>
    <li>
      <svg viewBox="0 0 16 16" aria-hidden="true"><circle cx="8" cy="8" r="7.3" fill="none" stroke="#fff"/><circle cx="8" cy="8" r="4" fill="none" stroke="#fff"/><path d="M4 8 H12 M8 4 V12" stroke="#fff"/></svg>
      www.lanternguide.org
    </li>
  </ul>
</section>

<section class="card card-back" aria-label="Card back">
  <div class="back-texture" role="img" aria-label="Subtle tonal damask pattern across the card back"
       style="background: radial-gradient(ellipse at 50% 45%, #4039a8 0%, var(--indigo) 55%, var(--indigo-deep) 100%);"></div>
  <div class="back-brand">
    <span class="brand-the">THE</span>
    <span class="brand-main">Lantern Guide</span>
    <span class="back-web">www.lanternguideweb.org</span>
  </div>
</section>

</body>
</html>
```